Attractive door board for entrance beautysalon

Make an attractive design for a board that can be glued on the front door of a beauty salon. The salon location has no window in the front so I need something catchy and attractive. The door board contains a list of the services and the website: www.velmora.be, and the text "Enkel op afspraak, bel 0486319542"

Target Market(s)

woman between 16 and 99 years old

Industry/Entity Type

Beauty Salon

Font styles to use
Sans Serif

Requirements
Must have
• A very nice, attractive but sober design.
• It must have a classy Marvaux, Quen, ... chique design.
• The logo must be on it (in attachment)
• There must be the following list in it:
• Gelaatsverzorging
• Wimperverlenging
• Wimperlifting
• Suikerontharing
• Permanente Make Up
• Airbrush Tanning
• Manicure - Pedicure - Tovira
• and then the website www.velmora.be, and the text "Enkel op afspraak, bel 0486319542"
Nice to have
• a catchy design,
• max. width can be 75 cm and max height 180 cm as it is a design for a board that will be glued on a door.
Should not have
• orchid flowers, buddha look a likes

```html
<!DOCTYPE html>
<html lang="nl">
<head>
<meta charset="utf-8">
<title>Velmora – deurbord</title>
<link href="https://fonts.googleapis.com/css2?family=Arimo:wght@400;700&display=swap" rel="stylesheet">
<style>
  :root {
    --paper: #ffffff;
    --ink: #111111;
    --accent: #e3202b;
    --frame: #8a8a8a;
    --photo-light: #e9e9e9;
    --photo-mid: #c9c9c9;
    --photo-dark: #9c9c9c;
  }
  html, body {
    margin: 0;
    padding: 0;
    overflow: hidden;
    background: var(--paper);
  }
  .door-board {
    position: relative;
    width: 1200px;
    height: 2880px;
    background: var(--paper);
    font-family: "Arimo", Helvetica, Arial, sans-serif;
    color: var(--ink);
    overflow: hidden;
  }
  .brand-square {
    position: absolute;
    left: 525px;
    top: 440px;
    width: 150px;
    height: 150px;
    box-sizing: border-box;
    border: 3px solid var(--ink);
  }
  .brand-name,
  .brand-tagline {
    position: absolute;
    left: 228px;
    width: 744px;
    margin: 0;
    display: flex;
    justify-content: space-between;
    font-weight: 400;
    line-height: 1;
  }
  .brand-name {
    top: 724px;
    font-size: 64px;
  }
  .brand-tagline {
    top: 836px;
    font-size: 20px;
  }
  .portrait-frame {
    position: absolute;
    left: 343px;
    top: 938px;
    width: 519px;
    height: 521px;
    margin: 0;
    box-sizing: border-box;
    border: 2px solid var(--frame);
    background: var(--paper);
  }
  .portrait-fill {
    position: absolute;
    left: 22px;
    top: 22px;
    right: 22px;
    bottom: 22px;
    background: radial-gradient(ellipse at 50% 45%, var(--photo-mid) 0%, var(--photo-light) 60%, var(--photo-light) 100%),
                linear-gradient(180deg, var(--photo-light), var(--photo-dark));
  }
  .service-list {
    position: absolute;
    left: 0;
    width: 100%;
    top: 1543px;
    margin: 0;
    padding: 0;
    list-style: none;
    text-align: center;
    font-weight: 700;
    font-size: 58px;
    line-height: 77px;
  }
  .website {
    position: absolute;
    left: 0;
    width: 100%;
    top: 2207px;
    margin: 0;
    text-align: center;
    font-size: 46px;
    color: var(--accent);
    line-height: 1.2;
  }
  .appointment {
    position: absolute;
    left: 0;
    width: 100%;
    top: 2327px;
    margin: 0;
    text-align: center;
    font-size: 45px;
    line-height: 1.2;
  }
</style>
</head>
<body>
  <main class="door-board">
    <div class="brand-square" aria-hidden="true"></div>

    <h1 class="brand-name" aria-label="Velmora">
      <span>V</span><span>E</span><span>L</span><span>M</span><span>O</span><span>R</span><span>A</span>
    </h1>
    <p class="brand-tagline" aria-label="Schoonheidsinstituut">
      <span>S</span><span>C</span><span>H</span><span>O</span><span>O</span><span>N</span><span>H</span><span>E</span><span>I</span><span>D</span><span>S</span><span>I</span><span>N</span><span>S</span><span>T</span><span>I</span><span>T</span><span>U</span><span>U</span><span>T</span>
    </p>

    <figure class="portrait-frame">
      <div class="portrait-fill" role="img" aria-label="Zwart-witfoto van een vrouw met gesloten ogen die haar schouder omarmt"></div>
    </figure>

    <ul class="service-list">
      <li>Gelaatsverzorging</li>
      <li>Wimperverlenging</li>
      <li>Wimperlifting</li>
      <li>Suikerontharing</li>
      <li>Permanente Make Up</li>
      <li>Airbrush Tanning</li>
      <li>Manicure - Pedicure - Tovira</li>
    </ul>

    <p class="website">www.velmora.be</p>
    <p class="appointment">Enkel op afspraak, bel 0486319542</p>
  </main>
</body>
</html>
```